Bref créative
MOBILE ULTRASOUND BUSINESS
Professional
Nora K. Pellway Hussel
President and Director of Ultrasound
517 Thornbury Lane #2614
Millbrook Twp. PA. 15832
nora@keystonepulsescanworks.example
keystonepulsescanworks.example
We need business cards for my husband as well, all info will be the same except for his name is Gavin P. Hussel - Chief Operating Officer for title - and gavin@keystonepulsescanworks.example
vector logo file

```html
<!DOCTYPE html>
<html lang="en">
<head>
<meta charset="utf-8">
<title>Keystone Pulse Scan Works – Stationery</title>
<link href="https://fonts.googleapis.com/css2?family=Roboto:wght@400;700&display=swap" rel="stylesheet">
<style>
:root{
  --ink:#0e0e0e;
  --blue:#1d8fd8;
  --green:#7cc242;
  --paper:#ffffff;
  --stage:#e6e6e6;
  --rule:#9a9a9a;
  --window:#c9c9c9;
  --label:#333333;
}
*{box-sizing:border-box;margin:0;padding:0}
html,body{width:1200px;height:410px;overflow:hidden}
body{background:var(--stage);font-family:"Roboto",Arial,sans-serif;position:relative}
.piece{position:absolute}
.brand{display:flex;align-items:center;gap:4px;color:var(--blue);font-weight:700;text-transform:uppercase;line-height:1.05}
.brand-mark{width:8px;height:8px;background:var(--blue);flex:none}

/* large envelope */
.envelope{left:20px;top:20px;width:340px;height:375px}
.envelope svg{position:absolute;left:0;top:0}
.envelope .body-brand{position:absolute;left:24px;top:232px;font-size:12px;width:140px}
.envelope .body-brand .brand-mark{width:13px;height:13px}
.envelope .flap-brand{position:absolute;left:104px;top:36px;transform:rotate(90deg);transform-origin:left top;font-size:10px;width:130px}
.envelope .flap-brand .brand-mark{width:11px;height:11px}
.envelope .return{position:absolute;left:24px;top:300px;color:var(--green);font-size:5px;line-height:1.6}
.envelope .window{position:absolute;left:200px;top:296px;width:118px;height:26px;background:var(--window)}

/* business cards */
.card{width:92px;height:52px;background:var(--ink);overflow:hidden}
.card .band{position:absolute;left:0;right:0;bottom:0;height:4px;background:var(--blue)}
.card .band::after{content:"";position:absolute;left:0;right:0;top:-2px;height:2px;background:var(--green)}
.card-front .brand{position:absolute;left:8px;top:16px;font-size:6px;width:76px}
.card-front .brand-mark{width:6px;height:6px}
.card-back .brand{position:absolute;left:4px;top:5px;font-size:3.4px;width:22px;gap:2px}
.card-back .brand-mark{width:4px;height:4px}
.card-info{position:absolute;right:4px;top:5px;text-align:right;color:var(--green);font-size:3.2px;line-height:1.45;width:62px;white-space:nowrap}
.card-info .name{color:var(--paper);font-weight:700;font-size:4px}

/* tall envelope */
.dl-envelope{left:576px;top:12px;width:80px;height:382px}
.dl-envelope .brand{position:absolute;left:10px;top:34px;font-size:6px;width:60px}
.dl-envelope .brand-mark{width:6px;height:6px}

/* sheets */
.sheet{background:var(--paper);box-shadow:0 1px 3px rgba(0,0,0,.25)}
.sheet-head{position:absolute;left:0;right:0;top:0;height:34px;background:var(--ink)}
.sheet-head .brand{position:absolute;left:10px;top:8px;font-size:7px;width:110px}
.sheet-head .brand-mark{width:9px;height:9px}
.sheet-head .contact{position:absolute;right:10px;top:6px;text-align:right;color:var(--green);font-size:3.6px;line-height:1.5}
.sheet-foot{position:absolute;left:0;right:0;bottom:0;height:10px;background:var(--ink);border-top:3px solid var(--blue)}

.fax{left:670px;top:20px;width:220px;height:375px}
.fax h1{position:absolute;left:14px;top:52px;font-size:14px;font-weight:700;color:var(--ink)}
.fax-fields{position:absolute;left:14px;top:80px;width:192px;display:grid;grid-template-columns:1fr 1fr;column-gap:12px;row-gap:6px}
.fax-field{display:flex;align-items:flex-end;gap:3px;font-size:4.5px;color:var(--label)}
.fax-field .line{flex:1;border-bottom:.6px solid var(--rule);height:5px}
.fax-checks{position:absolute;left:14px;top:128px;width:192px;display:flex;justify-content:space-between;font-size:3.8px;color:var(--label)}
.fax-checks i{display:inline-block;width:3.5px;height:3.5px;border:.5px solid var(--label);margin-right:1.5px;vertical-align:middle}
.fax-comments{position:absolute;left:14px;top:142px;font-size:4.5px;color:var(--label)}

.letterhead{left:910px;top:20px;width:220px;height:375px}
.letterhead .contact-side{position:absolute;right:62px;top:218px;color:var(--green);font-size:3.6px;line-height:1.5;text-align:right}

/* disc */
.disc{left:1012px;top:166px;width:176px;height:176px}
.disc .brand{position:absolute;left:120px;top:60px;font-size:4px;width:46px}
.disc .brand-mark{width:5px;height:5px}
</style>
</head>
<body>

<!-- large envelope with open flap -->
<div class="piece envelope">
  <svg width="340" height="375" viewBox="0 0 340 375">
    <polygon points="0,160 0,0 110,0 135,160" fill="#0e0e0e"/>
    <polygon points="110,0 119,0 144,160 135,160" fill="#1d8fd8"/>
    <rect x="0" y="160" width="340" height="215" fill="#0e0e0e"/>
    <polygon points="0,160 340,160 340,200 0,175" fill="#1d8fd8"/>
    <polygon points="0,175 340,200 340,204 0,179" fill="#7cc242"/>
    <rect x="0" y="366" width="340" height="9" fill="#1d8fd8"/>
  </svg>
  <div class="brand flap-brand"><span class="brand-mark"></span>Keystone Pulse Scan Works</div>
  <div class="brand body-brand"><span class="brand-mark"></span>Keystone Pulse Scan Works</div>
  <div class="return">517 Thornbury Lane #2614<br>Millbrook Twp. PA. 15832<br>412.555.0148<br>keystonepulsescanworks.example</div>
  <div class="window"></div>
</div>

<!-- business cards -->
<div class="piece card card-front" style="left:374px;top:24px">
  <div class="brand"><span class="brand-mark"></span>Keystone Pulse Scan Works</div>
  <div class="band"></div>
</div>
<div class="piece card card-back" style="left:472px;top:24px">
  <div class="brand"><span class="brand-mark"></span>Keystone Pulse Scan Works</div>
  <div class="card-info">
    <div class="name">Nora K. Pellway Hussel</div>
    President and Director of Ultrasound<br>
    517 Thornbury Lane #2614<br>Millbrook Twp. PA. 15832<br>
    412.555.0148<br>nora@keystonepulsescanworks.example<br>keystonepulsescanworks.example
  </div>
  <div class="band"></div>
</div>
<div class="piece card card-front" style="left:374px;top:84px">
  <div class="brand"><span class="brand-mark"></span>Keystone Pulse Scan Works</div>
  <div class="band"></div>
</div>
<div class="piece card card-back" style="left:472px;top:84px">
  <div class="brand"><span class="brand-mark"></span>Keystone Pulse Scan Works</div>
  <div class="card-info">
    <div class="name">Gavin P. Hussel</div>
    Chief Operating Officer<br>
    517 Thornbury Lane #2614<br>Millbrook Twp. PA. 15832<br>
    412.555.0148<br>gavin@keystonepulsescanworks.example<br>keystonepulsescanworks.example
  </div>
  <div class="band"></div>
</div>

<!-- tall envelope -->
<div class="piece dl-envelope">
  <svg width="80" height="382" viewBox="0 0 80 382">
    <rect width="80" height="382" fill="#0e0e0e"/>
    <polygon points="0,0 80,0 40,22" fill="#1d8fd8"/>
    <rect x="22" y="80" width="30" height="280" fill="#ffffff"/>
    <rect x="0" y="374" width="80" height="8" fill="#1d8fd8"/>
  </svg>
  <div class="brand"><span class="brand-mark"></span>Keystone Pulse Scan Works</div>
</div>

<!-- fax sheet -->
<div class="piece sheet fax">
  <div class="sheet-head">
    <div class="brand"><span class="brand-mark"></span>Keystone Pulse Scan Works</div>
    <div class="contact">517 Thornbury Lane #2614<br>Millbrook Twp. PA. 15832<br>412.555.0148<br>keystonepulsescanworks.example</div>
  </div>
  <h1>FAX</h1>
  <div class="fax-fields">
    <div class="fax-field">To:<span class="line"></span></div>
    <div class="fax-field">From:<span class="line"></span></div>
    <div class="fax-field">Fax:<span class="line"></span></div>
    <div class="fax-field">Pages:<span class="line"></span></div>
    <div class="fax-field">Phone:<span class="line"></span></div>
    <div class="fax-field">Date:<span class="line"></span></div>
    <div class="fax-field">Re:<span class="line"></span></div>
    <div class="fax-field">CC:<span class="line"></span></div>
  </div>
  <div class="fax-checks">
    <span><i></i>Urgent</span><span><i></i>For Review</span><span><i></i>Please Comment</span><span><i></i>Please Reply</span><span><i></i>Please Recycle</span>
  </div>
  <div class="fax-comments">Comments:</div>
  <div class="sheet-foot"></div>
</div>

<!-- letterhead -->
<div class="piece sheet letterhead">
  <div class="sheet-head">
    <div class="brand"><span class="brand-mark"></span>Keystone Pulse Scan Works</div>
  </div>
  <div class="contact-side">517 Thornbury Lane #2614<br>Millbrook Twp. PA. 15832<br>412.555.0148<br>keystonepulsescanworks.example</div>
  <div class="sheet-foot"></div>
</div>

<!-- disc -->
<div class="piece disc">
  <svg width="176" height="176" viewBox="0 0 176 176">
    <circle cx="88" cy="88" r="88" fill="#0e0e0e"/>
    <circle cx="88" cy="88" r="34" fill="#8a8a8a"/>
    <circle cx="88" cy="88" r="12" fill="#e6e6e6"/>
  </svg>
  <div class="brand"><span class="brand-mark"></span>Keystone Pulse Scan Works</div>
</div>

</body>
</html>
```